Letterhead Design Project

Looking for letterhead designs for Brastova Mining.

I am looking for a letterhead design in conjunction with a business card design. I have opened contests for both but ask that if you submit a letterhead design you also submit a business card design with a corresponding look/feel.

Brastova Mining is a B2B company that buys and sells large machinery tires within the coal mining industry. The design should the strong, crisp and masculine. I have uploaded the company logo and mock-up of the back of the company's business card.

Color scheme should be grey/green/black

Contact information to include:
Name: Dale Whitford
Title: Managing Director
Phone: 555-231-4097
Address: 1817 Pellam #3 Dallas, TX 75290
Email: Dale@Brastova.example
Updates

Project Deadline Extended
Reason: Looking for a more refined, elegant letterhead than what's been submitted as of yet. Here is a sample of what we're looking for: http://www.plumcrestgallery.example/letterhead-designs/ We will also be increasing the payment.

Industry/Entity Type

Coal Mining

```html
<!DOCTYPE html>
<html lang="en">
<head>
<meta charset="utf-8">
<title>Brastova Mining – Stationery Proof</title>
<link rel="stylesheet" href="https://fonts.googleapis.com/css2?family=Archivo+Black&family=Questrial&family=Roboto+Slab:wght@700&display=swap">
<style>
  :root {
    --paper: #ffffff;
    --ink-frame: #1a1a1a;
    --brand-green: #6f9a5e;
    --contact-grey: #7a7a7a;
    --card-dark: #1b1b1b;
    --card-mid: #2e2e2e;
    --card-text: #8c8c8c;
    --label-ink: #222222;
  }
  * { margin: 0; padding: 0; box-sizing: border-box; }
  html, body {
    width: 1139px;
    height: 1200px;
    overflow: hidden;
    background: var(--paper);
  }
  .proof-sheet {
    position: relative;
    width: 1139px;
    height: 1200px;
  }
  .proof-label {
    position: absolute;
    top: 14px;
    right: 23px;
    text-align: right;
    font-family: "Questrial", sans-serif;
    font-size: 13.5px;
    line-height: 17px;
    color: var(--label-ink);
    text-transform: uppercase;
  }
  .proof-label .proof-date { margin-bottom: 19px; }

  /* Letterhead */
  .letterhead {
    position: absolute;
    left: 10px;
    top: 215px;
    width: 745px;
    height: 964px;
    border: 1px solid var(--ink-frame);
    background: var(--paper);
  }
  .letterhead-name {
    position: absolute;
    top: 30px;
    left: 0;
    right: 0;
    text-align: center;
    font-family: "Archivo Black", sans-serif;
    font-size: 24px;
    line-height: 30px;
    color: var(--brand-green);
    text-transform: uppercase;
  }
  .letterhead-contact {
    position: absolute;
    top: 101px;
    left: 0;
    right: 0;
    text-align: center;
    font-family: "Archivo Black", sans-serif;
    font-size: 9.9px;
    color: var(--contact-grey);
    text-transform: uppercase;
    white-space: nowrap;
  }

  /* Business card */
  .business-card {
    position: absolute;
    left: 815px;
    top: 532px;
    width: 307px;
    height: 174px;
    overflow: hidden;
  }
  .card-surface {
    position: absolute;
    inset: 0;
    background: linear-gradient(135deg, var(--card-mid) 0%, var(--card-dark) 55%, var(--card-mid) 100%);
  }
  .card-name {
    position: absolute;
    top: 38px;
    left: 0;
    right: 0;
    text-align: center;
    font-family: "Archivo Black", sans-serif;
    font-size: 20px;
    line-height: 26px;
    color: var(--brand-green);
    text-transform: uppercase;
  }
  .card-contact {
    position: absolute;
    top: 122px;
    left: 0;
    right: 0;
    text-align: center;
    font-family: "Roboto Slab", serif;
    font-weight: 700;
    font-size: 8.6px;
    line-height: 10.5px;
    color: var(--card-text);
    text-transform: uppercase;
  }
</style>
</head>
<body>
<main class="proof-sheet">
  <header class="proof-label">
    <p class="proof-date">10–5–13</p>
    <p>Brastova Mining_v1</p>
    <p>Logo Proof</p>
    <p>Business Card Proof</p>
    <p>Letter Head Proof</p>
  </header>

  <section class="letterhead" aria-label="Letterhead">
    <p class="letterhead-name">Brastova Mining</p>
    <p class="letterhead-contact">Dale Whitford| Managing Director | 1817 Pellam #3 Dallas, TX 75290 | 555.231.4097 | Dale@Brastova.example</p>
  </section>

  <section class="business-card" aria-label="Business card">
    <div class="card-surface" role="img" aria-label="Dark charcoal textured card background"></div>
    <p class="card-name">Brastova Mining</p>
    <div class="card-contact">
      <p>Dale Whitford Managing Director</p>
      <p>1817 Pellam #3, Dallas, TX 75290</p>
      <p>555.231.4097</p>
      <p>Dale@Brastova.example</p>
    </div>
  </section>
</main>
</body>
</html>
```